Vantor 7 Skins

Hey I need 2 stickers made one for my vantor 7 Rower and one for my vantor 7 dyn arc.I have attached some images of the rower and dyn arc as well as some photos of the rower and ski with some stickers already done.And i have attached my logo so you can get a feel for how i would like it designed and the logos that need to be included.

Target Market(s)

TO BE STUCK ON THE MACHINES IN A GYM

The rowers will need to be reversable.

Font styles to use
Serif
Sans Serif
Other font styles liked:
• LATO

Colors
0392cd
33a6d7
85cae6
ffffff
0255a3
3176b5
cedeed
85acd3
e34197

```html
<!DOCTYPE html>
<html lang="en">
<head>
<meta charset="utf-8">
<title>Sticker Version 04 – Client: Corelift</title>
<link rel="stylesheet" href="https://fonts.googleapis.com/css2?family=Poppins:wght@300;400;600&family=Oswald:wght@500&display=swap">
<style>
  :root {
    --ink: #000000;
    --paper: #ffffff;
    --machine-light: #eceef1;
    --machine-dark: #d5d9de;
    --navy: #1f3fa6;
    --navy-deep: #0255a3;
    --royal: #3176b5;
    --sky: #0392cd;
    --sky-mid: #33a6d7;
    --sky-pale: #85cae6;
    --mist: #cedeed;
  }
  * { box-sizing: border-box; margin: 0; padding: 0; }
  html, body { width: 1200px; height: 1200px; overflow: hidden; background: var(--paper); }
  body { position: relative; font-family: "Poppins", sans-serif; color: var(--ink); }

  .board-header {
    position: absolute; left: 0; top: 0; width: 1200px; height: 107px;
    background: var(--ink); color: var(--paper);
    display: flex; align-items: center; justify-content: space-between;
    padding: 0 38px 0 46px;
    font-weight: 300; font-size: 37px; letter-spacing: 0.2px;
  }

  .option { position: absolute; left: 0; width: 1200px; height: 420px; }
  .option--one { top: 160px; }
  .option--two { top: 625px; }

  .mockup { position: absolute; left: 0; top: 0; width: 1200px; height: 420px; z-index: 1; }

  .option-label {
    position: absolute; left: 78px; top: 202px; z-index: 2;
    font-size: 17px; font-weight: 300; white-space: nowrap;
  }
  .option-label strong { font-weight: 600; margin-right: 4px; }

  .sticker-name { font-family: "Oswald", sans-serif; font-weight: 500; fill: var(--paper); }
  .sticker-tag  { font-family: "Oswald", sans-serif; font-weight: 500; fill: var(--mist); }
</style>
</head>
<body>

<header class="board-header">
  <span class="board-title">Sticker Version 04</span>
  <span class="board-client">Client: Corelift</span>
</header>

<section class="option option--one">
  <svg class="mockup" viewBox="0 0 1200 420" xmlns="http://www.w3.org/2000/svg">
    <defs>
      <linearGradient id="machineTone1" x1="0" y1="0" x2="1" y2="1">
        <stop offset="0" stop-color="var(--machine-light)"/>
        <stop offset="1" stop-color="var(--machine-dark)"/>
      </linearGradient>
    </defs>
    <polygon role="img" aria-label="Photo of an air rowing machine in side view, black frame with flywheel and grey seat"
      points="155,268 700,268 850,185 775,5 805,5 880,95 1035,95 1035,408 920,408 905,300 700,330 640,335 200,318 200,395 155,395"
      fill="url(#machineTone1)"/>
    <g class="sticker" transform="translate(167 272) rotate(1.2)">
      <rect x="0" y="0" width="460" height="46" fill="var(--paper)"/>
      <polygon points="0,4 190,4 205,24 460,24 455,40 190,40 180,46 0,46" fill="var(--navy)"/>
      <polygon points="0,4 30,4 12,30 0,30" fill="var(--royal)"/>
      <polygon points="170,4 200,4 220,16 190,16" fill="var(--royal)"/>
      <polygon points="400,14 430,14 405,46 375,46" fill="var(--sky)"/>
      <polygon points="436,14 460,14 460,30 422,46 410,46" fill="var(--sky-pale)"/>
      <text class="sticker-name" x="58" y="34" font-size="19" letter-spacing="1">CORELIFT</text>
      <text class="sticker-tag" x="222" y="37" font-size="11.5">PERSONAL &amp; GROUP TRAINING</text>
    </g>
  </svg>
  <p class="option-label"><strong>Option 01</strong> (Corelift logo on dark blue bg)</p>
</section>

<section class="option option--two">
  <svg class="mockup" viewBox="0 0 1200 420" xmlns="http://www.w3.org/2000/svg">
    <defs>
      <linearGradient id="machineTone2" x1="0" y1="0" x2="1" y2="1">
        <stop offset="0" stop-color="var(--machine-light)"/>
        <stop offset="1" stop-color="var(--machine-dark)"/>
      </linearGradient>
      <linearGradient id="lightPanel" x1="0" y1="0" x2="1" y2="0">
        <stop offset="0" stop-color="var(--sky)"/>
        <stop offset="1" stop-color="var(--royal)"/>
      </linearGradient>
    </defs>
    <polygon role="img" aria-label="Photo of an air rowing machine in side view, black frame with flywheel and grey seat"
      points="155,268 700,268 850,185 775,5 805,5 880,95 1035,95 1035,408 920,408 905,300 700,330 640,335 200,318 200,395 155,395"
      fill="url(#machineTone2)"/>
    <g class="sticker" transform="translate(167 277) rotate(1.2)">
      <rect x="0" y="0" width="460" height="46" fill="var(--paper)"/>
      <polygon points="0,12 170,12 190,4 460,4 460,30 190,30 180,46 0,46" fill="url(#lightPanel)"/>
      <polygon points="0,4 40,4 30,12 0,12" fill="var(--sky-pale)"/>
      <polygon points="150,12 200,12 185,22 140,22" fill="var(--navy-deep)"/>
      <polygon points="395,14 425,14 400,46 370,46" fill="var(--navy-deep)"/>
      <polygon points="432,14 460,14 460,30 420,46 408,46" fill="var(--sky-mid)"/>
      <text class="sticker-name" x="58" y="38" font-size="19" letter-spacing="1">CORELIFT</text>
      <text class="sticker-tag" x="222" y="24" font-size="11.5">PERSONAL &amp; GROUP TRAINING</text>
    </g>
  </svg>
  <p class="option-label"><strong>Option 02</strong> (Corelift logo on light blue bg)</p>
</section>

</body>
</html>
```